Handouts in brochure which included about our services, magnet card and emergency sticker design

We need a brochure packaging design for our company which is based in Australia. We are a home appliance services company based in Melbourne. We provide mainly three core services, Electrician, plumbing and building services/handyman.

We wish to include the following things in the brochure package we send to our customers :
1. About our services (4 sided bi fold design)
2. Magnet card
3. Emergency sticker for one of our services

We have already made a rough design of the content for each for this, however it needs designing and editing.

I have attached the files for your reference. You can visit http://corvale.net.au/
for more information.

Target Market(s)

30 to 40 years

Industry/Entity Type

Appliance

Font styles to use
Serif
Sans Serif

Colors
3176b5
fbed22
0456a4

Requirements
Must have
• Home
Nice to have
• Cars

```html
<!DOCTYPE html>
<html lang="en">
<head>
<meta charset="utf-8">
<title>Corvale's Home Services Flyer</title>
<link rel="stylesheet" href="https://fonts.googleapis.com/css2?family=Montserrat:wght@500;600;700&display=swap">
<style>
  :root {
    --bg: #3f3f3f;
    --paper: #ffffff;
    --brand-blue: #0a6aad;
    --ink-blue: #0d4f8b;
    --brand-yellow: #fbdc05;
    --band-yellow: rgba(240, 200, 10, 0.85);
  }
  * { margin: 0; padding: 0; box-sizing: border-box; }
  html, body {
    width: 1200px; height: 1200px; overflow: hidden;
    background: var(--bg);
    font-family: 'Montserrat', sans-serif;
  }
  .flyer {
    position: absolute; left: 229px; top: 59px;
    width: 762px; height: 1082px;
    background: var(--paper);
    overflow: hidden;
  }
  .hero-photo {
    position: absolute; left: 0; top: 0; width: 762px; height: 587px;
    background: linear-gradient(180deg, #c9d3de 0%, #d8cfc8 28%, #7d6a5e 52%, #4d4a48 78%, #3a3a3c 100%);
  }
  .hero-band {
    position: absolute; left: 0; top: 34px; width: 762px; height: 31px;
    background: var(--band-yellow);
  }
  .rule-blue {
    position: absolute; left: 0; top: 587px; width: 762px; height: 14px;
    background: var(--brand-blue);
  }
  .rule-yellow {
    position: absolute; left: 0; width: 762px; height: 4px;
    background: var(--brand-yellow);
  }
  .rule-yellow.upper { top: 601px; }
  .rule-yellow.lower { top: 902px; }
  .services {
    position: absolute; left: 59px; top: 634px; width: 642px;
    display: grid;
    grid-template-columns: repeat(6, 107px);
    grid-template-rows: 134px 134px;
  }
  .service {
    display: flex; flex-direction: column; align-items: center;
    text-align: center;
  }
  .service svg { width: 50px; height: 44px; margin-bottom: 26px; }
  .service-label {
    color: var(--ink-blue);
    font-weight: 500; font-size: 14.5px; line-height: 22px;
    white-space: nowrap; letter-spacing: -0.3px;
  }
  .tagline-panel {
    position: absolute; left: 0; top: 906px; width: 762px; height: 109px;
    background: var(--brand-blue);
    display: flex; align-items: center; justify-content: center;
  }
  .tagline {
    color: var(--brand-yellow);
    font-weight: 700; font-size: 22px; line-height: 33px;
    text-align: center; letter-spacing: -0.4px;
  }
  .web-bar {
    position: absolute; left: 0; top: 1015px; width: 762px; height: 30px;
    background: var(--brand-yellow);
    display: flex; align-items: center; justify-content: center;
    color: var(--ink-blue); font-weight: 700; font-size: 18px;
  }
</style>
</head>
<body>
<main class="flyer">
  <div class="hero-photo" role="img" aria-label="Photo of the company's branded white service van parked in front of a brick house, with hot air balloons in the evening sky"></div>
  <div class="hero-band"></div>
  <div class="rule-blue"></div>
  <div class="rule-yellow upper"></div>

  <section class="services">
    <div class="service">
      <svg viewBox="0 0 60 52" fill="none" stroke="#1a1a1a" stroke-width="2.5"><path d="M6 27 L30 5 L54 27"/><path d="M12 22 V48 H48 V22"/><path d="M25 48 V34 H35 V48"/><path d="M40 14 V8 H45 V18"/></svg>
      <span class="service-label">HOME</span>
    </div>
    <div class="service">
      <svg viewBox="0 0 60 52" fill="none" stroke="#1a1a1a" stroke-width="2.5"><rect x="3" y="6" width="54" height="40"/><rect x="8" y="11" width="22" height="30"/><rect x="14" y="24" width="10" height="10" fill="#1a1a1a"/><path d="M16 24 V20 a3 3 0 0 1 6 0 V24"/><g fill="#1a1a1a" stroke="none"><circle cx="37" cy="14" r="2"/><circle cx="44" cy="14" r="2"/><circle cx="51" cy="14" r="2"/><circle cx="37" cy="22" r="2"/><circle cx="44" cy="22" r="2"/><circle cx="51" cy="22" r="2"/><circle cx="37" cy="30" r="2"/><circle cx="44" cy="30" r="2"/><circle cx="51" cy="30" r="2"/><circle cx="44" cy="38" r="2"/></g></svg>
      <span class="service-label">SECURITY</span>
    </div>
    <div class="service">
      <svg viewBox="0 0 60 52" fill="#1a1a1a"><rect x="2" y="16" width="6" height="20"/><path d="M8 20 H36 a12 12 0 0 1 12 12 V38 H38 V32 a2 2 0 0 0 -2 -2 H8 Z"/><rect x="22" y="9" width="6" height="11"/><rect x="16" y="5" width="18" height="4"/><path d="M43 42 q-3 5 0 6 q3 -1 0 -6z"/></svg>
      <span class="service-label">PLUMBING</span>
    </div>
    <div class="service">
      <svg viewBox="0 0 60 52" fill="none" stroke="#1a1a1a" stroke-width="2"><circle cx="30" cy="26" r="22"/><path d="M24 24 a6 6 0 1 1 12 0 c0 4 -3 5 -3 9 h-6 c0 -4 -3 -5 -3 -9z"/><path d="M27 37 H33 M28 40 H32"/><path d="M30 33 V26"/></svg>
      <span class="service-label">ELECTRICAL</span>
    </div>
    <div class="service">
      <svg viewBox="0 0 60 52" fill="none" stroke="#1a1a1a" stroke-width="2.5"><path d="M14 4 V34 a10 10 0 0 0 20 0 V30 a5 5 0 0 1 10 0"/><path d="M22 4 V34 a2 2 0 0 0 4 0 V30 a13 13 0 0 1 26 0"/><path d="M12 4 H24"/></svg>
      <span class="service-label">DRAINS</span>
    </div>
    <div class="service">
      <svg viewBox="0 0 60 52" fill="#1a1a1a"><rect x="16" y="4" width="16" height="8" rx="3"/><path d="M8 50 V38 q0 -12 16 -14 q16 2 16 14 V50 Z"/><path d="M40 26 l12 12 l-3 3 l-12 -12z"/><circle cx="51" cy="22" r="5" fill="none" stroke="#1a1a1a" stroke-width="3"/></svg>
      <span class="service-label">HANDYMAN<br>SERVICES</span>
    </div>

    <div class="service">
      <svg viewBox="0 0 60 52" fill="none" stroke="#1a1a1a" stroke-width="2.5"><rect x="14" y="18" width="32" height="26"/><path d="M22 36 V28 L30 22 L38 28 V36 Z" fill="#1a1a1a"/><rect x="12" y="8" width="10" height="8" fill="#1a1a1a"/><rect x="38" y="8" width="10" height="8" fill="#1a1a1a"/><circle cx="8" cy="28" r="5"/><circle cx="52" cy="28" r="5"/></svg>
      <span class="service-label">CAMERA<br>SYSTEMS</span>
    </div>
    <div class="service">
      <svg viewBox="0 0 60 52" fill="none" stroke="#1a1a1a" stroke-width="2.5"><path d="M44 14 V6 H54 V12"/><path d="M22 18 l14 -6 l8 8 l-6 14 z" fill="#1a1a1a"/><g stroke-width="2" stroke-dasharray="2 3"><path d="M26 30 L10 46"/><path d="M22 26 L4 40"/><path d="M30 34 L16 50"/></g></svg>
      <span class="service-label">HOT WATER<br>SYSTEMS</span>
    </div>
    <div class="service">
      <svg viewBox="0 0 60 52" fill="none" stroke="#1a1a1a" stroke-width="2"><rect x="2" y="6" width="56" height="20" rx="2"/><path d="M6 20 H54 M6 23 H54"/><path d="M22 32 q-2 3 0 6 q2 3 0 6 M30 32 q-2 3 0 6 q2 3 0 6 M38 32 q-2 3 0 6 q2 3 0 6" stroke-width="1.5"/></svg>
      <span class="service-label">AIR<br>CONDITIONING</span>
    </div>
    <div class="service">
      <svg viewBox="0 0 60 52" fill="none" stroke="#1a1a1a" stroke-width="2"><rect x="18" y="8" width="10" height="16"/><path d="M21 4 V8 M25 4 V8"/><path d="M23 24 V40 a6 6 0 0 0 12 0 V34"/><rect x="32" y="26" width="10" height="12"/><path d="M35 38 V42 M39 38 V42"/></svg>
      <span class="service-label">DATA<br>CABLING</span>
    </div>
    <div class="service">
      <svg viewBox="0 0 60 52" fill="#1a1a1a"><path d="M14 12 l14 -4 l6 6 l-4 4 l-4 -2 l-6 2 z"/><path d="M26 16 l4 4 l-18 20 l-4 -4 z"/><g stroke="#1a1a1a" stroke-width="2"><path d="M40 6 l4 -4 M44 12 l6 -2 M42 18 l6 2"/></g></svg>
      <span class="service-label">CARPENTRY</span>
    </div>
    <div class="service">
      <svg viewBox="0 0 60 52" fill="none" stroke="#1a1a1a" stroke-width="3"><path d="M6 26 L30 4 L54 26"/><path d="M12 20 V48 H48 V20"/><path d="M30 44 c-8 0 -10 -8 -4 -16 c0 4 2 6 4 6 c-1 -5 2 -10 6 -12 c-2 6 4 10 2 16 c-1 4 -4 6 -8 6z" fill="#1a1a1a" stroke="none"/></svg>
      <span class="service-label">GAS<br>FITTING</span>
    </div>
  </section>

  <div class="rule-yellow lower"></div>
  <div class="tagline-panel">
    <p class="tagline">WE LOVE OUR JOBS,VALUE OUR CUSTOMERS AND<br>TREAT EVERY HOME AS IF IT WERE OUR OWN.</p>
  </div>
  <div class="web-bar">corvale.net.au</div>
</main>
</body>
</html>
```